looking to have a web site for the company which provides services in the industrial and commercial sectors such as: electrical, automation control and system integration, construction and maintenance, millwright, equipment assembly repair and installation. I have the domain already brivanholdings.net and logo. Most recent projects fulfilled for the following clients: MarlowKibbleCo, Dunholt University, OKSU, FALSTO, Tazzik, Prairie Grains

Target Market(s)

industrial and commercial sectors in electrical, automation, millwright and fabrication fields

Industry/Entity Type

Industrial

Coding

Coded - Design and coding required

Number of Pages Required

5+ page

Font styles to use
Sans Serif

Colors

Designer to choose colors to be used in the design.

Requirements
Nice to have
• looking to get something not complicated, nicely presented with minimum or no scrolling

```html
<!DOCTYPE html>
<html lang="en">
<head>
<meta charset="utf-8">
<title>Brivan Holdings — Services, Industry &amp; Testimonials</title>
<link rel="stylesheet" href="https://fonts.googleapis.com/css2?family=Poppins:wght@400;500&family=Roboto:wght@300;400;500&display=swap">
<style>
  :root {
    --blue: #0a6aa8;
    --blue-card: #0b6fad;
    --quote: #a8d2ee;
    --bg: #ebebeb;
    --bg-light: #f3f3f3;
    --text: #6a6a6a;
    --dark: #333333;
    --white: #ffffff;
  }
  * { box-sizing: border-box; margin: 0; padding: 0; }
  html, body { width: 1200px; height: 1200px; overflow: hidden; }
  body { background: var(--bg); font-family: "Roboto", sans-serif; position: relative; }

  .services { position: absolute; left: 0; top: 0; width: 1200px; height: 364px; background: var(--bg); }
  .service { position: absolute; top: 0; width: 286px; }
  .service__photo { height: 69px; width: 286px; }
  .service__title { margin-top: 19px; font-family: "Poppins", sans-serif; font-weight: 500; font-size: 14px; line-height: 18px; color: var(--blue); min-height: 46px; }
  .service__text { margin-top: 0; font-weight: 300; font-size: 11.4px; line-height: 16.5px; color: var(--text); }
  .btn { display: inline-block; background: var(--blue); color: var(--white); font-family: "Roboto", sans-serif; font-weight: 500; font-size: 11.5px; height: 32px; line-height: 32px; width: 99px; text-align: center; text-decoration: none; }
  .service .btn { position: absolute; top: 198px; left: -3px; }
  .btn--outline { position: absolute; left: 497px; top: 276px; width: 207px; height: 36px; line-height: 34px; background: transparent; border: 1px solid var(--blue); color: var(--blue); font-family: "Poppins", sans-serif; font-size: 13px; letter-spacing: 0.5px; }

  .industry { position: absolute; left: 0; top: 364px; width: 1200px; height: 485px; background: var(--bg-light); }
  .industry__photo { position: absolute; left: 0; top: 0; width: 601px; height: 485px; background: linear-gradient(135deg, #cfd2d3 0%, #8e9396 45%, #5a5f63 100%); }
  .industry__body { position: absolute; left: 682px; top: 104px; width: 370px; }
  .industry__title { font-family: "Poppins", sans-serif; font-weight: 400; font-size: 31px; line-height: 36px; color: var(--blue); }
  .industry__lead { margin-top: 10px; font-family: "Poppins", sans-serif; font-size: 13.6px; line-height: 18.5px; color: var(--dark); }
  .industry__text { margin-top: 14px; font-weight: 300; font-size: 11.4px; line-height: 16.5px; color: var(--text); }
  .industry .btn { margin-top: 29px; }

  .testimonials { position: absolute; left: 0; top: 849px; width: 1200px; height: 351px; background: var(--bg); }
  .testimonials__title { position: absolute; top: 30px; width: 100%; text-align: center; font-family: "Poppins", sans-serif; font-weight: 400; font-size: 32px; color: var(--dark); }
  .testimonials__title span { color: var(--blue); }
  .testimonial { position: absolute; top: 89px; width: 286px; height: 240px; }
  .testimonial__card { position: absolute; left: 0; top: 0; width: 286px; height: 191px; background: var(--blue-card); border-radius: 6px; }
  .testimonial__tail { position: absolute; left: 0; top: 190px; }
  .testimonial__open { position: absolute; left: 16px; top: 21px; }
  .testimonial__close { position: absolute; right: 12px; top: 137px; }
  .testimonial__text { position: absolute; left: 20px; top: 65px; width: 255px; color: var(--white); font-size: 11.6px; line-height: 16.5px; font-weight: 400; }
  .testimonial__avatar { position: absolute; left: -1px; top: 162px; width: 66px; height: 66px; border-radius: 50%; border: 3px solid var(--white); background: linear-gradient(160deg, #c9b8a8, #6d5a50); }
  .testimonial__name { position: absolute; left: 98px; top: 200px; font-size: 11.8px; font-weight: 500; color: var(--dark); }
  .testimonial__role { position: absolute; left: 98px; top: 214px; font-size: 10px; color: #8a8a8a; }
</style>
</head>
<body>

<section class="services">
  <article class="service" style="left:150px">
    <div class="service__photo" role="img" aria-label="Electrical panel with warning labels" style="background:linear-gradient(180deg,#b9b8b2,#8f8e88)"></div>
    <h3 class="service__title">Electrical</h3>
    <p class="service__text">Aliquam varius, leo ac aliquet fringilla, urna sapien tie odio, et vulputate dui felis et leo. Aliquam et malesuada nibh. Vivamus sit amet bibendum nunc,</p>
    <a class="btn" href="#">READ MORE</a>
  </article>
  <article class="service" style="left:459px">
    <div class="service__photo" role="img" aria-label="Control cabinet with PLC modules" style="background:linear-gradient(180deg,#8d9095,#c4c6c8)"></div>
    <h3 class="service__title">Automation Control and System Integration</h3>
    <p class="service__text">Aliquam varius, leo ac aliquet fringilla, urna sapien tie odio, et vulputate dui felis et leo. Aliquam et malesuada nibh. Vivamus sit amet bibendum nunc,</p>
    <a class="btn" href="#">READ MORE</a>
  </article>
  <article class="service" style="left:763px">
    <div class="service__photo" role="img" aria-label="Industrial machinery under construction" style="background:linear-gradient(180deg,#5e6350,#a3a25c)"></div>
    <h3 class="service__title">Construction and Maintenance</h3>
    <p class="service__text">Aliquam varius, leo ac aliquet fringilla, urna sapien tie odio, et vulputate dui felis et leo. Aliquam et malesuada nibh. Vivamus sit amet bibendum nunc,</p>
    <a class="btn" href="#">READ MORE</a>
  </article>
  <a class="btn btn--outline" href="#">VIEW ALL SERVICES</a>
</section>

<section class="industry">
  <div class="industry__photo" role="img" aria-label="Stainless steel process tanks and control panel in a plant"></div>
  <div class="industry__body">
    <h2 class="industry__title">INDUSTRY</h2>
    <p class="industry__lead">Fusce efficitur lectus et ante porta, sodales ultricies purus eleifend. Suspendisse arcu purus</p>
    <p class="industry__text">Etiam ac tempor metus, nec pretium diam. Integer in aliquet odio. Praesent quis congue quam. Nullam libero sem, tincidunt a nisl quis, sollicitudin malesuada erat. Aliquam luctus pellentesque lobortis. Curabitur non enim ut orci posuere sodales. Proin a magna leo. Curabitur pulvinar nisl sed justo faucibus ornare. Ut et fermentum enim. Vestibulum vel porttitor dui, in facilisis magna. Quisque semper augue in tortor placerat, vel vestibulum sem laoreet.</p>
    <a class="btn" href="#">READ MORE</a>
  </div>
</section>

<section class="testimonials">
  <h2 class="testimonials__title"><span>CLIENT</span> TESTIMONIALS</h2>

  <article class="testimonial" style="left:150px">
    <div class="testimonial__card"></div>
    <svg class="testimonial__tail" width="120" height="22" viewBox="0 0 120 22"><polygon points="84,0 118,0 71,20" fill="var(--blue-card)"/></svg>
    <svg class="testimonial__open" width="40" height="28" viewBox="0 0 40 28" fill="var(--quote)"><path d="M1 28V15C1 6 6 1 14 0v6c-4 1-6 3-6 7h6v15z"/><path d="M22 28V15c0-9 5-14 13-15v6c-4 1-6 3-6 7h6v15z"/></svg>
    <svg class="testimonial__close" width="40" height="28" viewBox="0 0 40 28" fill="var(--quote)"><path d="M18 0v13c0 9-5 14-13 15v-6c4-1 6-3 6-7H5V0z"/><path d="M39 0v13c0 9-5 14-13 15v-6c4-1 6-3 6-7h-6V0z"/></svg>
    <p class="testimonial__text">Aliquam et malesuada nibh. Vivamus sit amet biben nunc, at dapibus nulla. Maecenas sollicitudin pellen quam. Duis placerat aliquam eros eu. Ut eu mollis lacus. Nam nec luctus nibh, snunc.</p>
    <div class="testimonial__avatar" role="img" aria-label="Client portrait"></div>
    <p class="testimonial__name">Lorem ipsum</p>
    <p class="testimonial__role">Dolor sit amet</p>
  </article>

  <article class="testimonial" style="left:458px">
    <div class="testimonial__card"></div>
    <svg class="testimonial__tail" width="120" height="22" viewBox="0 0 120 22"><polygon points="84,0 118,0 71,20" fill="var(--blue-card)"/></svg>
    <svg class="testimonial__open" width="40" height="28" viewBox="0 0 40 28" fill="var(--quote)"><path d="M1 28V15C1 6 6 1 14 0v6c-4 1-6 3-6 7h6v15z"/><path d="M22 28V15c0-9 5-14 13-15v6c-4 1-6 3-6 7h6v15z"/></svg>
    <svg class="testimonial__close" width="40" height="28" viewBox="0 0 40 28" fill="var(--quote)"><path d="M18 0v13c0 9-5 14-13 15v-6c4-1 6-3 6-7H5V0z"/><path d="M39 0v13c0 9-5 14-13 15v-6c4-1 6-3 6-7h-6V0z"/></svg>
    <p class="testimonial__text">Aliquam et malesuada nibh. Vivamus sit amet biben nunc, at dapibus nulla. Maecenas sollicitudin pellen quam. Duis placerat aliquam eros eu. Ut eu mollis lacus. Nam nec luctus nibh, snunc.</p>
    <div class="testimonial__avatar" role="img" aria-label="Client portrait" style="background:linear-gradient(160deg,#d9d6d2,#8b7a6e)"></div>
    <p class="testimonial__name">Fusce efficitur</p>
    <p class="testimonial__role">Dolor sit amet</p>
  </article>

  <article class="testimonial" style="left:765px">
    <div class="testimonial__card"></div>
    <svg class="testimonial__tail" width="120" height="22" viewBox="0 0 120 22"><polygon points="84,0 118,0 71,20" fill="var(--blue-card)"/></svg>
    <svg class="testimonial__open" width="40" height="28" viewBox="0 0 40 28" fill="var(--quote)"><path d="M1 28V15C1 6 6 1 14 0v6c-4 1-6 3-6 7h6v15z"/><path d="M22 28V15c0-9 5-14 13-15v6c-4 1-6 3-6 7h6v15z"/></svg>
    <svg class="testimonial__close" width="40" height="28" viewBox="0 0 40 28" fill="var(--quote)"><path d="M18 0v13c0 9-5 14-13 15v-6c4-1 6-3 6-7H5V0z"/><path d="M39 0v13c0 9-5 14-13 15v-6c4-1 6-3 6-7h-6V0z"/></svg>
    <p class="testimonial__text">Aliquam et malesuada nibh. Vivamus sit amet biben nunc, at dapibus nulla. Maecenas sollicitudin pellen quam. Duis placerat aliquam eros eu. Ut eu mollis lacus. Nam nec luctus nibh, snunc.</p>
    <div class="testimonial__avatar" role="img" aria-label="Client portrait" style="background:linear-gradient(160deg,#cfc9cc,#7d6b66)"></div>
    <p class="testimonial__name">Mauris facilisis</p>
    <p class="testimonial__role">Dolor sit amet</p>
  </article>
</section>

</body>
</html>
```